lawncare business

Lawncare business. Definitely need company name( Pemberdale) and slogan ( When your grass gets tall, give us a call) and of course contact info..I would like a unique logo that is lawncare related and alot of attention getting color on the card.

Industry/Entity Type

Business

Contact Information for Business Card

Owner: Marcus Dellow Pemberdale
(555) 814-2260 When your grass gets tall, give us a call.

Requirements
Must have
• Unique lawncare related logo......company name and slogan.....Contact info

```html
<!DOCTYPE html>
<html lang="en">
<head>
<meta charset="utf-8">
<title>Pemberdale Business Cards</title>
<link href="https://fonts.googleapis.com/css2?family=Fira+Sans:wght@300;400;700&display=swap" rel="stylesheet">
<style>
  :root {
    --page-bg: #e9ebe8;
    --card-white: #f7f7f5;
    --green-dark: #108a3e;
    --green-band: #22a457;
    --green-light: #8cc63f;
    --band-text: #d8f0c4;
  }
  * { margin: 0; padding: 0; box-sizing: border-box; }
  html, body { width: 1200px; height: 873px; overflow: hidden; }
  body {
    background: var(--page-bg);
    font-family: "Fira Sans", sans-serif;
    position: relative;
  }
  .card {
    position: absolute;
    top: 293px;
    width: 500px;
    height: 286px;
    background: var(--card-white);
    box-shadow: 0 6px 18px rgba(0,0,0,0.15);
    overflow: hidden;
  }
  .card--band { left: 70px; }
  .card--plain { left: 630px; }

  .brand {
    position: absolute;
    left: 150px;
    top: 48px;
    display: flex;
    align-items: center;
    gap: 12px;
  }
  .brand__square {
    width: 36px;
    height: 36px;
    background: var(--green-dark);
  }
  .brand__name {
    font-weight: 700;
    font-size: 30px;
    letter-spacing: 0.5px;
    color: var(--green-dark);
    text-transform: uppercase;
  }

  .person {
    position: absolute;
    left: 0;
    width: 100%;
    top: 118px;
    text-align: center;
  }
  .person__name {
    font-weight: 700;
    font-size: 22px;
    color: var(--green-dark);
  }
  .person__role {
    font-weight: 400;
    font-size: 13px;
    color: var(--green-light);
    margin-top: 3px;
  }

  .band {
    position: absolute;
    left: 0;
    bottom: 0;
    width: 100%;
    height: 72px;
    background: var(--green-band);
  }
  .slogan {
    font-weight: 300;
    font-size: 10px;
    line-height: 1.35;
  }
  .band .slogan {
    position: absolute;
    left: 18px;
    top: 16px;
    color: var(--band-text);
  }
  .band .phone {
    position: absolute;
    right: 40px;
    top: 18px;
    color: var(--band-text);
  }
  .phone {
    font-weight: 300;
    font-size: 30px;
    letter-spacing: 0.5px;
  }

  .card--plain .slogan {
    position: absolute;
    left: 18px;
    top: 20px;
    color: var(--green-dark);
  }
  .card--plain .phone {
    position: absolute;
    left: 0;
    width: 100%;
    text-align: center;
    top: 205px;
    color: var(--green-band);
  }
</style>
</head>
<body>

  <section class="card card--band">
    <div class="brand">
      <span class="brand__square"></span>
      <span class="brand__name">Pemberdale</span>
    </div>
    <div class="person">
      <p class="person__name">Marcus Dellow</p>
      <p class="person__role">Owner</p>
    </div>
    <div class="band">
      <p class="slogan">When your grass gets tall,<br>give us a call !</p>
      <p class="phone">(555) 814-2260</p>
    </div>
  </section>

  <section class="card card--plain">
    <p class="slogan">When your grass gets tall,<br>give us a call !</p>
    <div class="brand">
      <span class="brand__square"></span>
      <span class="brand__name">Pemberdale</span>
    </div>
    <div class="person">
      <p class="person__name">Marcus Dellow</p>
      <p class="person__role">Owner</p>
    </div>
    <p class="phone">(555) 814-2260</p>
  </section>

</body>
</html>
```